Vivaform - Fitness Coach. Needs a Business Card Design that I can also use for other advertising

Established 2012, I have finished the QPLB National Certificate in Fitness & Personal Training. Harrowgate First Aid Certificate. I have the Auckland 800m track records for MW45. I also came 1st at the 2012 Pacifica Games in 800 & 1500m. I am passionate about health & fitness and would like to help people reach their health & fitness goals. I also take health & fitness weekends. Main interests - Running, Weight Training, Yoga & Aqua Jogging. I like strength/power, but am femine.

Target Market(s)

Male or Female 18 and over that wants to improve their health & fitness

Industry/Entity Type

Advertising

Requirements
Must have
• my name: Lorissa K Dunmore contact details: lori@brightpath.co.nz mobile - 021 579318 URL name: facebook.com/lorissaKdunmore - VivaForm
Photo of Me

```html
<!DOCTYPE html>
<html lang="en">
<head>
<meta charset="utf-8">
<title>Lorissa K Dunmore – Fitness Coach Business Card</title>
<link rel="stylesheet" href="https://fonts.googleapis.com/css2?family=Play:wght@400;700&display=swap">
<style>
  :root {
    --backdrop: #c9ad8a;
    --card-black: #000000;
    --ink-white: #ffffff;
    --foliage-dark: #2f4a1e;
    --foliage-mid: #4f7a2c;
    --foliage-light: #7ea345;
  }
  * { box-sizing: border-box; margin: 0; padding: 0; }
  html, body {
    width: 1200px;
    height: 985px;
    overflow: hidden;
    background: var(--backdrop);
  }
  .stage {
    position: relative;
    width: 1200px;
    height: 985px;
  }
  .card {
    position: absolute;
    background: var(--card-black);
    border-radius: 26px;
    color: var(--ink-white);
    font-family: "Play", "Trebuchet MS", sans-serif;
    overflow: hidden;
  }

  /* Front side */
  .card-front {
    left: 82px;
    top: 75px;
    width: 468px;
    height: 820px;
  }
  .front-name {
    position: absolute;
    top: 0;
    left: 0;
    width: 100%;
    height: 66px;
    line-height: 66px;
    text-align: center;
    font-weight: 700;
    font-size: 29px;
    letter-spacing: 0.5px;
  }
  .rule {
    position: absolute;
    left: 0;
    width: 100%;
    height: 4px;
    background: var(--ink-white);
  }
  .rule-top { top: 65px; }
  .rule-bottom { top: 758px; }
  .coach-photo {
    position: absolute;
    top: 73px;
    left: 0;
    width: 100%;
    height: 681px;
    background:
      radial-gradient(ellipse at 30% 25%, var(--foliage-light) 0%, transparent 55%),
      radial-gradient(ellipse at 70% 70%, var(--foliage-mid) 0%, transparent 60%),
      linear-gradient(180deg, var(--foliage-dark) 0%, var(--foliage-mid) 60%, var(--foliage-light) 100%);
  }
  .tagline {
    position: absolute;
    top: 770px;
    left: 0;
    width: 100%;
    text-align: center;
    font-size: 21px;
    font-weight: 400;
    letter-spacing: 0.3px;
  }

  /* Back side */
  .card-back {
    left: 621px;
    top: 82px;
    width: 466px;
    height: 817px;
  }
  .back-details {
    position: absolute;
    top: 303px;
    left: 0;
    width: 100%;
    text-align: center;
  }
  .back-name {
    font-weight: 700;
    font-size: 39px;
    letter-spacing: 0.6px;
    line-height: 48px;
  }
  .back-role {
    font-size: 28px;
    font-weight: 400;
    line-height: 36px;
    margin-top: 4px;
  }
  .contact-list {
    list-style: none;
    margin-top: 38px;
    font-size: 21px;
    line-height: 37px;
  }
  .contact-item {
    display: flex;
    justify-content: center;
    align-items: center;
    gap: 7px;
  }
  .contact-icon {
    width: 20px;
    height: 20px;
    flex: none;
  }
  .social-square {
    width: 18px;
    height: 18px;
    background: var(--ink-white);
    border-radius: 3px;
    flex: none;
  }
</style>
</head>
<body>
<main class="stage">
  <section class="card card-front">
    <h1 class="front-name">Lorissa K Dunmore</h1>
    <div class="rule rule-top"></div>
    <div class="coach-photo" role="img" aria-label="Photo of the coach leaping in the air in an orange top and black leggings in front of a green hedge"></div>
    <div class="rule rule-bottom"></div>
    <p class="tagline">meeting your health &amp; fitness goals</p>
  </section>

  <section class="card card-back">
    <div class="back-details">
      <h2 class="back-name">Lorissa K Dunmore</h2>
      <p class="back-role">Fitness Coach</p>
      <ul class="contact-list">
        <li class="contact-item">
          <svg class="contact-icon" viewBox="0 0 20 20" aria-hidden="true">
            <path d="M2 8 L10 3 L18 8 V16 H2 Z" fill="#fff"/>
            <path d="M2 8 L10 13 L18 8" fill="none" stroke="#000" stroke-width="1.6"/>
          </svg>
          <span>lori@brightpath.co.nz</span>
        </li>
        <li class="contact-item">
          <svg class="contact-icon" viewBox="0 0 20 20" aria-hidden="true">
            <rect x="5" y="1" width="10" height="18" rx="1.5" fill="#fff"/>
            <rect x="7" y="3.5" width="6" height="5" fill="#000"/>
            <rect x="7" y="10.5" width="2" height="1.5" fill="#000"/>
            <rect x="11" y="10.5" width="2" height="1.5" fill="#000"/>
            <rect x="7" y="13.5" width="2" height="1.5" fill="#000"/>
            <rect x="11" y="13.5" width="2" height="1.5" fill="#000"/>
          </svg>
          <span>021 579318</span>
        </li>
        <li class="contact-item">
          <span class="social-square" aria-hidden="true"></span>
          <span>Vivaform</span>
        </li>
      </ul>
    </div>
  </section>
</main>
</body>
</html>
```